Frame Glow Entertainment | Business Card & Logo

We are looking for a business card with a Logo.
It’s a brand new business and we are looking for an elegant design.
The business service categories are:
Photo Booth
Photography
Events Planning
Marcus Pellham
0471926358
0381736492
info@frameglowentertainment.com.au
www.frameglowentertainment.com.au
Target Market(s)
Corporate, Photo Booth, Photography and event planning
Industry/Entity Type
Photo Booth, Photography and event planning
Contact Information for Business Card
Marcus Pellham | 0471926358 | 0381736492 | info@frameglowentertainment.com.au | www.frameglowentertainment.com.au

```html
<!DOCTYPE html>
<html lang="en">
<head>
<meta charset="utf-8">
<title>Frame Glow Entertainment — Business Card</title>
<link rel="stylesheet" href="https://fonts.googleapis.com/css2?family=Montserrat:wght@400;500;700&display=swap">
<style>
  :root {
    --backdrop: #3a3a3a;
    --card-dark: #000000;
    --card-light: #ffffff;
    --brand-orange: #f7a400;
    --ink: #1a1a1a;
    --paper-text: #ffffff;
  }
  * { margin: 0; padding: 0; box-sizing: border-box; }
  html, body {
    width: 1200px;
    height: 998px;
    overflow: hidden;
    background: var(--backdrop);
    font-family: "Montserrat", sans-serif;
  }
  .stage {
    position: relative;
    width: 1200px;
    height: 998px;
  }
  .card {
    position: absolute;
    width: 560px;
    height: 320px;
    box-shadow: 0 14px 30px rgba(0,0,0,0.45);
  }
  .card--front {
    left: 80px;
    top: 100px;
    background: var(--card-dark);
  }
  .card--back {
    left: 560px;
    top: 580px;
    background: var(--card-light);
  }
  .brand-mark {
    display: flex;
    align-items: center;
    gap: 12px;
    color: var(--brand-orange);
    font-weight: 700;
    line-height: 1.05;
  }
  .brand-mark__dot {
    flex: none;
    border: 3px solid var(--brand-orange);
    border-radius: 50%;
  }
  .card--front .brand-mark {
    position: absolute;
    left: 150px;
    top: 92px;
    font-size: 26px;
  }
  .card--front .brand-mark__dot { width: 46px; height: 46px; }
  .tagline {
    position: absolute;
    left: 0;
    right: 0;
    top: 222px;
    text-align: center;
    color: var(--paper-text);
    font-size: 15px;
    font-weight: 400;
    letter-spacing: 0.3px;
  }
  .card--back .brand-mark {
    position: absolute;
    right: 34px;
    top: 34px;
    font-size: 20px;
  }
  .card--back .brand-mark__dot { width: 36px; height: 36px; }
  .rule {
    position: absolute;
    height: 1px;
    background: var(--ink);
  }
  .rule--top { left: 250px; right: 30px; top: 116px; }
  .holder {
    position: absolute;
    left: 34px;
    top: 168px;
    color: var(--brand-orange);
    font-size: 25px;
    font-weight: 700;
  }
  .rule--name { left: 34px; width: 330px; top: 206px; }
  .contact-list {
    position: absolute;
    left: 34px;
    top: 218px;
    list-style: none;
    color: var(--ink);
    font-size: 14px;
    font-weight: 400;
  }
  .contact-list li {
    display: flex;
    align-items: center;
    gap: 10px;
    height: 26px;
  }
  .contact-list svg { width: 15px; height: 15px; flex: none; }
</style>
</head>
<body>
<main class="stage">
  <section class="card card--front" aria-label="Card front">
    <div class="brand-mark">
      <span class="brand-mark__dot"></span>
      <span class="brand-mark__name">Frame Glow<br>Entertainment</span>
    </div>
    <p class="tagline">Photo Booth | Photography | Events Planning</p>
  </section>

  <section class="card card--back" aria-label="Card back">
    <div class="brand-mark">
      <span class="brand-mark__dot"></span>
      <span class="brand-mark__name">Frame Glow<br>Entertainment</span>
    </div>
    <div class="rule rule--top"></div>
    <h1 class="holder">Marcus Pellham</h1>
    <div class="rule rule--name"></div>
    <ul class="contact-list">
      <li>
        <svg viewBox="0 0 24 24" aria-hidden="true"><path fill="#1a1a1a" d="M6.6 10.8a15.1 15.1 0 0 0 6.6 6.6l2.2-2.2a1 1 0 0 1 1-.25 11.4 11.4 0 0 0 3.6.57 1 1 0 0 1 1 1V20a1 1 0 0 1-1 1A17 17 0 0 1 3 4a1 1 0 0 1 1-1h3.5a1 1 0 0 1 1 1c0 1.25.2 2.45.57 3.57a1 1 0 0 1-.25 1z"/></svg>
        <span>0471926358 | 0381736492</span>
      </li>
      <li>
        <svg viewBox="0 0 24 24" aria-hidden="true"><rect x="2" y="5" width="20" height="14" fill="#1a1a1a"/><path d="M2 5l10 8 10-8" fill="none" stroke="#fff" stroke-width="1.6"/></svg>
        <span>info@frameglowentertainment.com.au</span>
      </li>
      <li>
        <svg viewBox="0 0 24 24" aria-hidden="true"><g fill="none" stroke="#1a1a1a" stroke-width="2"><circle cx="12" cy="12" r="9.5"/><ellipse cx="12" cy="12" rx="4" ry="9.5"/><path d="M2.5 12h19M4 7h16M4 17h16"/></g></svg>
        <span>www.frameglowentertainment.com.au</span>
      </li>
    </ul>
  </section>
</main>
</body>
</html>
```